Bref créative
Stationary for Visual Explanation Business
Bus Card, Stationary
Professional
Martin Pelloway
CEO & Founder
487 E 29th Street, Suite 4B
New York, NY 10027
USA
martin@lumbrivista.com
www.lumbrivista.com
Looking for clean and modern sophisticated look and feel for a marketing service business company that offers visual explanations for technology companies. Not cutesy. A blend of QXR combined with creative agency.
The letterhead will serve as my proposal template. I will use it for placing text and illustrations.
I want to keep with the orange and gray of the logo.
I wil supply the AI version of the logo shortly.
Logo AI File with tagline and name
Logo Ai File with company name and no tagline
Logo Ai file with no tagline and no company name

```html
<!DOCTYPE html>
<html lang="en">
<head>
<meta charset="utf-8">
<title>Lumbrivista Stationery</title>
<link rel="stylesheet" href="https://fonts.googleapis.com/css2?family=Open+Sans:wght@400;600;700&display=swap">
<style>
  :root {
    --paper: #ffffff;
    --canvas: #ffffff;
    --slate: #6d7074;
    --slate-light: #9a9da1;
    --orange: #f0922e;
    --ink: #4a4c4f;
  }
  html, body {
    margin: 0;
    padding: 0;
    width: 1200px;
    height: 778px;
    overflow: hidden;
    background: var(--canvas);
    font-family: "Open Sans", Arial, sans-serif;
    color: var(--ink);
  }
  .set { position: relative; width: 1200px; height: 778px; }
  .sheet {
    position: absolute;
    background: var(--paper);
    box-shadow: 0 1px 4px rgba(0,0,0,.25);
    overflow: hidden;
  }
  .band { position: absolute; left: 0; top: 0; }
  address { font-style: normal; }
  .brand-name {
    position: absolute;
    margin: 0;
    font-weight: 700;
    color: var(--orange);
    letter-spacing: -.3px;
    line-height: 1;
    white-space: nowrap;
  }
  .brand-tagline {
    position: absolute;
    font-size: 5px;
    letter-spacing: .6px;
    text-transform: uppercase;
    color: var(--slate);
    white-space: nowrap;
  }

  /* Letterhead */
  .letterhead { left: 26px; top: 48px; width: 507px; height: 672px; }
  .letterhead .brand-name { left: 30px; top: 46px; font-size: 24px; }
  .letterhead .brand-tagline { left: 31px; top: 76px; }
  .letterhead-footer {
    position: absolute; left: 26px; bottom: 20px;
    font-size: 9px; line-height: 13px;
  }

  /* Business card */
  .card { left: 602px; top: 108px; width: 206px; height: 125px; }
  .card .brand-name { left: 12px; top: 12px; font-size: 12px; }
  .card .brand-tagline { left: 12px; top: 27px; font-size: 3px; }
  .card-person { position: absolute; left: 100px; top: 74px; width: 90px; text-align: center; }
  .card-name { font-size: 8px; font-weight: 600; }
  .card-title { font-size: 5px; color: var(--slate); }
  .card-contact { position: absolute; left: 8px; top: 66px; font-size: 4.5px; line-height: 7px; }

  /* Envelope */
  .envelope { left: 578px; top: 408px; width: 598px; height: 312px; }
  .envelope .brand-name { left: 28px; top: 124px; font-size: 24px; }
  .envelope .brand-tagline { left: 29px; top: 153px; }
  .envelope-address { position: absolute; left: 29px; top: 162px; font-size: 8.5px; line-height: 12px; }
</style>
</head>
<body>
<main class="set">

  <section class="sheet letterhead" aria-label="Letterhead">
    <svg class="band" width="507" height="120" viewBox="0 0 507 120" aria-hidden="true">
      <path d="M0 0 H507 V22 C420 24 290 20 190 26 C100 32 40 46 0 112 Z" fill="var(--slate-light)"/>
      <path d="M0 0 H507 V14 C420 16 290 12 190 18 C100 24 40 38 0 102 Z" fill="var(--slate)"/>
    </svg>
    <p class="brand-name">Lumbrivista</p>
    <div class="brand-tagline">Visual explanations for technology</div>
    <address class="letterhead-footer">
      487 E 29th Street, Suite 4B, New York, NY 10027, USA<br>
      Phone: (212) 555-0148<br>
      Email: martin@lumbrivista.com | www.lumbrivista.com
    </address>
  </section>

  <section class="sheet card" aria-label="Business card">
    <svg class="band" width="206" height="44" viewBox="0 0 206 44" aria-hidden="true">
      <path d="M0 0 H206 V6 C150 7 90 6 50 9 C25 11 10 18 0 40 Z" fill="var(--slate)"/>
    </svg>
    <p class="brand-name">Lumbrivista</p>
    <div class="brand-tagline">Visual explanations for technology</div>
    <div class="card-person">
      <div class="card-name">Martin Pelloway</div>
      <div class="card-title">CEO &amp; Founder</div>
    </div>
    <address class="card-contact">
      487 E 29th Street, Suite 4B<br>
      New York, NY 10027, USA<br>
      Phone: (212) 555-0148<br>
      Email: martin@lumbrivista.com<br>
      www.lumbrivista.com
    </address>
  </section>

  <section class="sheet envelope" aria-label="Envelope">
    <svg class="band" width="598" height="130" viewBox="0 0 598 130" aria-hidden="true">
      <path d="M0 18 Q0 0 18 0 H580 Q598 0 598 18 V74 C520 74 320 68 200 72 C110 76 40 86 0 128 Z" fill="var(--slate-light)"/>
      <path d="M0 18 Q0 0 18 0 H580 Q598 0 598 18 V66 C520 66 320 60 200 64 C110 68 40 78 0 118 Z" fill="var(--slate)"/>
    </svg>
    <p class="brand-name">Lumbrivista</p>
    <div class="brand-tagline">Visual explanations for technology</div>
    <address class="envelope-address">
      487 E 29th Street, Suite 4B<br>
      New York, NY 10027, USA
    </address>
  </section>

</main>
</body>
</html>
```